Business cards

Design business cards for our company. Just a straight, business like design with the logo, name, function and contact details

Target Market(s)

We are a innovative technological company active in water treatment

Industry/Entity Type

Water management

Contact Information for Business Card

Name, Function, email, telephone number, link to website

```html
<!DOCTYPE html>
<html lang="en">
<head>
<meta charset="utf-8">
<title>Aqualon7 Business Cards</title>
<link href="https://fonts.googleapis.com/css2?family=Exo+2:wght@400;500&display=swap" rel="stylesheet">
<style>
  :root {
    --backdrop: #c9ccd0;
    --brand-blue: #3a9ad9;
    --brand-blue-light: #5fb2e3;
    --card-white: #f4f5f6;
    --ink-grey: #7d8186;
    --edge-blue: #2a86cf;
  }
  * { margin: 0; padding: 0; box-sizing: border-box; }
  html, body { width: 1200px; height: 900px; overflow: hidden; }
  body {
    background: var(--backdrop);
    font-family: "Exo 2", sans-serif;
    display: flex;
    align-items: center;
    justify-content: center;
    gap: 60px;
  }
  .card {
    width: 490px;
    height: 280px;
    position: relative;
    border-bottom: 6px solid var(--edge-blue);
  }
  .card-front {
    background: linear-gradient(160deg, var(--brand-blue-light), var(--brand-blue));
    display: flex;
    align-items: center;
    justify-content: center;
  }
  .wordmark {
    display: flex;
    align-items: center;
    gap: 12px;
    font-weight: 400;
    letter-spacing: 1px;
  }
  .wordmark-dot {
    width: 30px; height: 30px; border-radius: 50%;
  }
  .card-front .wordmark { color: #ffffff; font-size: 46px; }
  .card-front .wordmark-dot { background: #ffffff; }
  .card-back { background: var(--card-white); }
  .card-back .wordmark {
    position: absolute; left: 34px; top: 48px;
    color: var(--brand-blue); font-size: 34px;
  }
  .card-back .wordmark-dot { background: var(--brand-blue); width: 22px; height: 22px; }
  .holder { position: absolute; left: 34px; top: 128px; }
  .holder-name {
    color: var(--brand-blue); font-size: 17px; font-weight: 500;
    letter-spacing: 1px; text-transform: uppercase;
  }
  .holder-role { color: var(--ink-grey); font-size: 12px; letter-spacing: 1px; }
  .contacts {
    position: absolute; left: 34px; top: 186px;
    list-style: none; color: var(--ink-grey);
    font-size: 12.5px; letter-spacing: 1.5px; line-height: 21px;
  }
  .contacts li { display: flex; align-items: center; gap: 8px; }
  .contacts svg { width: 11px; height: 11px; fill: var(--brand-blue); }
</style>
</head>
<body>
  <section class="card card-front">
    <div class="wordmark"><span>Aqualon7</span><span class="wordmark-dot"></span></div>
  </section>

  <section class="card card-back">
    <div class="wordmark"><span>Aqualon7</span><span class="wordmark-dot"></span></div>
    <div class="holder">
      <p class="holder-name">Petros Valianos</p>
      <p class="holder-role">Director</p>
    </div>
    <ul class="contacts">
      <li>
        <svg viewBox="0 0 12 12" aria-hidden="true"><path d="M2.5 0.5l2 2.3-1 1.2c.6 1.6 2 3 3.5 3.6l1.2-1 2.3 2-1.2 2.4C4.5 10.8 1.2 7.5 0.1 2.5z"/></svg>
        <span>07900 482 615</span>
      </li>
      <li>
        <svg viewBox="0 0 12 12" aria-hidden="true"><path d="M0 2h12v8H0z M0.8 2.6L6 6.6l5.2-4" fill="none" stroke="var(--brand-blue)" stroke-width="1.4"/></svg>
        <span>info@aqualon7.com</span>
      </li>
      <li>
        <svg viewBox="0 0 12 12" aria-hidden="true"><circle cx="6" cy="6" r="5.2" fill="none" stroke="var(--brand-blue)" stroke-width="1.2"/><path d="M0.8 6h10.4M6 0.8c-3 3-3 7.4 0 10.4M6 0.8c3 3 3 7.4 0 10.4" fill="none" stroke="var(--brand-blue)" stroke-width="1"/></svg>
        <span>www.aqualon7.com</span>
      </li>
    </ul>
  </section>
</body>
</html>
```